Advertisement Sign Project

Hi there,

I have a commercial space available for short term lease.

I need an advertisement sign to go on the double black doors (under the current Veldora Quinsprit sign).

The advertising sign should be about A3 in size and designed to attract pedestrians.

See site address at 417 Brambury Street Richmond Victoria Australia:

https://maps.wembrolink.com.au/view?q=417B+Brambury+St,+Richmond+Victoria+3121&ll=-37.800000,144.900000&z=17

Target Market(s)

Pop-up store tenants: fashion, textiles, bedding, furniture, homewares and kitchenwares.

The photos are provided to give you (the graphic designer) an idea of the space available.

Industry/Entity Type

Advertising

Requirements
Must have
• Retail tenancy available for short term lease.

For all enquiries contact Morton - 0417362908 or email morton@bramburylanehub.com.au

Nice to have
• Something befitting the look and feel of the building.

I was thinking a textile pattern as background, or some kind of fashion design element to inspire a potential pop up shop tenant.

```html
<!DOCTYPE html>
<html lang="en">
<head>
<meta charset="utf-8">
<title>Commercial Space Available – Short Term Lease Sign</title>
<link rel="stylesheet" href="https://fonts.googleapis.com/css2?family=Stardos+Stencil:wght@700&family=Open+Sans:wght@400;600&display=swap">
<style>
  :root {
    --page-grey: #e2e2e2;
    --brick-light: #b0705a;
    --brick-mid: #8a4a3a;
    --brick-deep: #5a3028;
    --night: #262222;
    --headline-white: #fbf8f2;
    --glow-amber: #ffb43a;
    --glow-orange: #ee7d14;
    --bubble-orange: #f06a22;
    --bubble-amber: #f7a338;
    --card-light: #f2f2f2;
    --card-mid: #a9a9a9;
    --card-dark: #7c7c7c;
    --footer-text: #f2f2f2;
  }
  * { margin: 0; padding: 0; box-sizing: border-box; }
  html, body { width: 1000px; height: 1200px; overflow: hidden; }
  body { background: var(--page-grey); position: relative; }

  .poster {
    position: absolute; left: 95px; top: 18px;
    width: 817px; height: 1137px; overflow: hidden;
    background: var(--night);
  }
  .poster__backdrop { position: absolute; inset: 0; }

  .paint-splash {
    position: absolute; left: 42px; top: 0; width: 108px; height: 110px;
    background: var(--headline-white);
    clip-path: polygon(22% 0, 58% 10%, 100% 32%, 84% 55%, 92% 82%, 42% 100%, 6% 96%, 14% 70%, 0 45%, 16% 30%);
  }

  .headline { position: absolute; inset: 0; font-size: inherit; }
  .headline__line {
    position: absolute; white-space: nowrap;
    font-family: "Stardos Stencil", "Black Ops One", sans-serif;
    font-weight: 700; line-height: 1;
    color: var(--headline-white);
    text-shadow: 0 0 5px var(--glow-amber), 0 0 14px var(--glow-orange), 0 0 26px rgba(238,125,20,.55);
    transform-origin: left center;
  }
  .headline__line--commercial { left: 20px; top: 150px; font-size: 118px; letter-spacing: -3px; transform: rotate(-7deg) scaleY(1.15); }
  .headline__line--space { left: 115px; top: 283px; font-size: 106px; letter-spacing: -2px; transform: rotate(-3deg) scaleY(1.35); }
  .headline__line--available { left: 45px; top: 407px; font-size: 118px; letter-spacing: -4px; transform: rotate(8deg) scaleY(1.3); }

  .sector-card {
    position: absolute; width: 124px; height: 170px;
    border: 3px solid #fff;
    box-shadow: 4px 6px 10px rgba(0,0,0,.5);
  }
  .sector-card--bedding { left: 72px; top: 565px; transform: rotate(7deg) skewY(-5deg);
    background: linear-gradient(160deg, var(--card-light) 0%, #cfcfcf 45%, var(--card-dark) 60%, #e6e6e6 75%, var(--card-mid)); }
  .sector-card--cookware { left: 112px; top: 688px; transform: rotate(6deg) skewY(-5deg);
    background: radial-gradient(circle at 45% 45%, #fafafa 0, #bdbdbd 35%, #6e6e6e 55%, #e0e0e0 75%); }
  .sector-card--fashion { left: 172px; top: 812px; transform: rotate(7deg) skewY(-5deg);
    background: linear-gradient(180deg, var(--card-light) 0, #d6d6d6 35%, var(--card-dark) 65%, #cfcfcf); }
  .sector-card--textile { left: 262px; top: 930px; width: 120px; height: 145px; transform: rotate(7deg) skewY(-5deg);
    background: linear-gradient(135deg, #d9d9d9, #9a9a9a 50%, #c8c8c8); }

  .lease-bubble { position: absolute; left: 475px; top: 872px; width: 225px; height: 225px; }
  .lease-bubble__text {
    position: absolute; left: 502px; top: 928px; width: 172px;
    font-family: "Open Sans", Arial, sans-serif; font-weight: 400;
    color: #fff; text-align: center; line-height: 1.05;
    transform: rotate(-14deg);
  }
  .lease-bubble__for { font-size: 24px; display: block; }
  .lease-bubble__term { font-size: 32px; display: block; }

  .enquiries {
    position: absolute; left: 0; right: 0; top: 1096px;
    text-align: center;
    font-family: "Open Sans", Arial, sans-serif; font-size: 16.8px;
    color: var(--footer-text);
  }
</style>
</head>
<body>
  <main class="poster">
    <svg class="poster__backdrop" width="817" height="1137" viewBox="0 0 817 1137" role="img" aria-label="Photograph of an aged red brick wall fading into shadow">
      <defs>
        <linearGradient id="brickTone" x1="0" y1="0" x2="1" y2="1">
          <stop offset="0" stop-color="var(--brick-mid)"/>
          <stop offset=".45" stop-color="var(--brick-light)"/>
          <stop offset="1" stop-color="var(--brick-deep)"/>
        </linearGradient>
        <linearGradient id="shadowFade" x1="0" y1="0" x2="0" y2="1">
          <stop offset="0" stop-color="var(--night)" stop-opacity="0"/>
          <stop offset="1" stop-color="var(--night)"/>
        </linearGradient>
      </defs>
      <rect width="817" height="1137" fill="url(#brickTone)"/>
      <path d="M0 560 C 260 640, 540 730, 817 790 L817 870 C 540 810, 260 720, 0 650 Z" fill="url(#shadowFade)"/>
      <path d="M0 648 C 260 718, 540 808, 817 866 L817 1137 L0 1137 Z" fill="var(--night)"/>
    </svg>

    <div class="paint-splash" role="img" aria-label="White paint splash"></div>

    <h1 class="headline">
      <span class="headline__line headline__line--commercial">COMMERCIAL</span>
      <span class="headline__line headline__line--space">SPACE</span>
      <span class="headline__line headline__line--available">AVAILABLE</span>
    </h1>

    <div class="sector-card sector-card--bedding" role="img" aria-label="Photo of a made bed with striped bedding"></div>
    <div class="sector-card sector-card--cookware" role="img" aria-label="Photo of stacked stainless steel cookware"></div>
    <div class="sector-card sector-card--fashion" role="img" aria-label="Illustration of a dress on a hanger"></div>
    <div class="sector-card sector-card--textile" role="img" aria-label="Photo of patterned textile fabric"></div>

    <svg class="lease-bubble" viewBox="0 0 225 225" aria-hidden="true">
      <defs>
        <linearGradient id="bubbleFill" x1="0" y1="1" x2="1" y2="0">
          <stop offset="0" stop-color="var(--bubble-orange)"/>
          <stop offset="1" stop-color="var(--bubble-amber)"/>
        </linearGradient>
      </defs>
      <g transform="rotate(-14 112 100)">
        <path d="M38 42 Q 44 16 80 14 L168 10 Q 204 10 207 45 L211 128 Q 213 163 180 166 L82 171 L52 214 L54 171 Q 26 169 25 140 Z"
              fill="url(#bubbleFill)" stroke="#fff" stroke-width="7" stroke-linejoin="round"
              style="filter: drop-shadow(3px 5px 5px rgba(0,0,0,.55))"/>
      </g>
    </svg>
    <p class="lease-bubble__text">
      <span class="lease-bubble__for">for</span>
      <span class="lease-bubble__term">Short Term</span>
      <span class="lease-bubble__term">Lease</span>
    </p>

    <p class="enquiries">For all enquiries contact Morton - 0417 362 908 or email morton@bramburylanehub.com.au</p>
  </main>
</body>
</html>
```